Finance Product Agency Business Card Design

We're an agency that provides products (service contracts, gap insurance, tire and wheel, etc) and support to dealership finance departments. We specialize in training finance producers to maximize their potential and also keep them up to date on the ever changing compliance and legal landscape. I'll attach an image of our logo, excited to see what you all come up with. Would also be interested in discussing our new website design with the winner.

Target Market(s)

auto dealerships

Industry/Entity Type

Business

Contact Information for Business Card

Dale Hoskirk
Phone 517.364.2908
Fax 877.245.3196
email Dale.Hoskirk@brightlanecoverage.com

Requirements
Must have
• basic contact information
Nice to have
• looking for something professional but modern

```html
<!DOCTYPE html>
<html lang="en">
<head>
<meta charset="utf-8">
<title>Brightlane Coverage – Business Card</title>
<link rel="stylesheet" href="https://fonts.googleapis.com/css2?family=Open+Sans:wght@400;600;700&display=swap">
<style>
  :root {
    --teal: #3e5f6e;
    --teal-dark: #34505d;
    --white: #ffffff;
    --grey: #8a8f93;
    --grey-light: #c9cdd0;
    --ink: #2f3b42;
    --stage: #e9ecee;
  }
  * { box-sizing: border-box; margin: 0; padding: 0; }
  html, body { width: 1200px; height: 900px; overflow: hidden; }
  body {
    background: var(--stage);
    font-family: "Open Sans", Arial, sans-serif;
    position: relative;
  }
  .card {
    position: absolute;
    left: 250px;
    width: 700px;
    height: 400px;
    border-radius: 22px;
    overflow: hidden;
    box-shadow: 0 6px 18px rgba(0,0,0,.18);
  }

  /* Back side */
  .card-back { top: 35px; background: var(--teal); }
  .card-back .foot-band {
    position: absolute; left: 0; bottom: 0; width: 100%; height: 60px;
  }
  .back-brand {
    position: absolute; left: 0; right: 0; top: 120px;
    display: flex; flex-direction: column; align-items: center; gap: 18px;
  }
  .back-brand .mark-dot {
    width: 64px; height: 64px; border-radius: 50%; background: var(--white);
  }
  .back-brand .brand-name {
    color: var(--white); font-weight: 700; font-size: 34px; letter-spacing: 1px;
  }
  .back-web {
    position: absolute; right: 34px; bottom: 78px;
    color: var(--white); font-size: 15px; letter-spacing: .3px;
  }

  /* Front side */
  .card-front { top: 465px; background: var(--white); }
  .front-brand {
    position: absolute; left: 40px; top: 58px;
    display: flex; align-items: center; gap: 14px;
  }
  .front-brand .mark-dot {
    width: 44px; height: 44px; border-radius: 50%; background: var(--teal);
  }
  .front-brand .brand-name {
    color: var(--teal); font-weight: 700; font-size: 30px; letter-spacing: .5px;
  }
  .holder {
    position: absolute; right: 40px; top: 128px; width: 270px;
    border-bottom: 2px solid var(--grey);
    text-align: right; padding-bottom: 4px;
    color: var(--teal); font-weight: 700; font-size: 26px;
  }
  .accent {
    position: absolute; left: 0; top: 0; width: 100%; height: 100%;
  }
  .front-web {
    position: absolute; right: 200px; top: 196px;
    color: var(--ink); font-size: 14px;
  }
  .contact {
    position: absolute; left: 40px; bottom: 34px; width: 300px;
    border-top: 1.5px solid var(--grey); padding-top: 10px;
    list-style: none; color: var(--ink); font-size: 15px; line-height: 1.35;
  }
  .contact li { display: flex; align-items: center; gap: 10px; }
  .contact svg { width: 14px; height: 14px; fill: var(--teal); flex: none; }
</style>
</head>
<body>

<section class="card card-back">
  <div class="back-brand">
    <span class="mark-dot"></span>
    <span class="brand-name">BRIGHTLANE COVERAGE</span>
  </div>
  <p class="back-web">www.brightlanecoverage.com</p>
  <svg class="foot-band" viewBox="0 0 700 60" preserveAspectRatio="none">
    <polygon points="0,28 430,28 450,8 700,8 700,60 0,60" fill="#ffffff"/>
  </svg>
</section>

<section class="card card-front">
  <svg class="accent" viewBox="0 0 700 400" preserveAspectRatio="none">
    <line x1="330" y1="222" x2="700" y2="222" stroke="#8a8f93" stroke-width="1.5"/>
    <polygon points="520,228 700,228 700,280 520,280" fill="#3e5f6e"/>
    <polygon points="500,228 520,228 520,280 490,280" fill="#c9cdd0"/>
  </svg>

  <div class="front-brand">
    <span class="mark-dot"></span>
    <span class="brand-name">BRIGHTLANE COVERAGE</span>
  </div>

  <h1 class="holder">Dale Hoskirk</h1>
  <p class="front-web">www.brightlanecoverage.com</p>

  <ul class="contact">
    <li>
      <svg viewBox="0 0 24 24"><path d="M6.6 10.8a15.1 15.1 0 0 0 6.6 6.6l2.2-2.2a1 1 0 0 1 1-.25 11.4 11.4 0 0 0 3.6.57 1 1 0 0 1 1 1V20a1 1 0 0 1-1 1A17 17 0 0 1 3 4a1 1 0 0 1 1-1h3.5a1 1 0 0 1 1 1c0 1.25.2 2.45.57 3.6a1 1 0 0 1-.25 1z"/></svg>
      517.364.2908
    </li>
    <li>
      <svg viewBox="0 0 24 24"><path d="M6 3h10v5H6zM3 9h18v9h-3v3H6v-3H3zm5 7v3h8v-3z"/></svg>
      877.245.3196
    </li>
    <li>
      <svg viewBox="0 0 24 24"><path d="M2 5h20v14H2zm2 2v.5l8 5 8-5V7zm0 2.8V17h16V9.8l-8 5z"/></svg>
      Dale.Hoskirk@brightlanecoverage.com
    </li>
  </ul>
</section>

</body>
</html>
```